Website re-design

We are a successful furnished apartment provider in Boston. We currently are working on re-designing our website www.ribtenlofts.com to make it more modern, designer look and user friendly. We hired a designer, but are not happy with the designs proposed and want to improve on them. The winning design will be paid regardless of whether we stay with our current designer or not. We want ideas and functional page links to see how it will work. Platform we have chosen is wordpress. Feel free to propose others easy for us to update and modify. We do not like Joomla on which website is currently running. We do not like flash nor long load times.
Please use photos on our website for design presentations. www.ribtenlofts.com

Target Market(s)

doctors, nurses, business men but mostly business women, some post-medical students

Industry/Entity Type

Apartment

Requirements
Must have
• Quick action button for reservation form and a notification and email forwarding system to us of reservation information by potential clients. Blog required with feedback by guests allowed, we can censor which are published. Slide shows of apartments.
Should not have
• No movies.

```html
<!DOCTYPE html>
<html lang="en">
<head>
<meta charset="utf-8">
<title>Ribten Lofts – Furnished Apartments</title>
<link href="https://fonts.googleapis.com/css2?family=Cinzel:wght@400;600&family=PT+Sans&display=swap" rel="stylesheet">
<style>
  :root{
    --bg:#0a0a0a;
    --gold:#c9b27a;
    --gold-dim:#a8925a;
    --gold-text:#9c8a5c;
    --nav-text:#a8925f;
    --muted:#4c4435;
    --muted-2:#6e6249;
    --cell-a:#121212;
    --cell-b:#1a1a1a;
    --cell-c:#151515;
    --cell-d:#0f0f0f;
    --arrow:#3a3a3a;
    --social:#27313f;
  }
  *{margin:0;padding:0;box-sizing:border-box}
  html,body{width:1200px;height:721px;overflow:hidden;background:var(--bg)}
  body{position:relative;font-family:"PT Sans",sans-serif;color:var(--gold-text)}
  .serif{font-family:"Cinzel",serif;font-weight:400}
  a{color:inherit;text-decoration:none}

  .nav-cell{position:absolute;height:57px;display:flex;align-items:center;justify-content:center;
    font-family:"Cinzel",serif;font-size:11.5px;font-weight:400;color:var(--nav-text);letter-spacing:.3px}
  .nav-cell.active{background:var(--gold);color:#1a1508;font-weight:600}
  .nav-sub{position:absolute;top:135px;font-family:"Cinzel",serif;font-size:11.5px;font-weight:600;color:var(--nav-text);letter-spacing:.2px;white-space:nowrap}

  .brand{position:absolute;left:248px;top:59px;display:flex;align-items:center;gap:10px}
  .brand-mark{width:46px;height:46px;border-radius:50%;background:var(--gold)}
  .brand-name{font-family:"Cinzel",serif;font-size:19px;color:var(--gold);letter-spacing:.5px;white-space:nowrap}

  .slide-photo{position:absolute;left:247px;top:174px;width:230px;height:229px;
    background:linear-gradient(135deg,#f2d9a8 0%,#e3a75a 45%,#b9773e 75%,#6b4226 100%)}
  .slide-arrow{position:absolute;top:281px}

  .welcome{position:absolute;left:553px;top:201px;font-size:23px;line-height:25px;color:var(--gold-dim);letter-spacing:.2px;white-space:nowrap}
  .intro{position:absolute;left:553px;top:274px;width:343px;font-size:9.6px;line-height:15.6px;text-align:justify;color:var(--gold-text)}
  .signoff{position:absolute;left:553px;top:358px;font-size:11.5px;color:var(--gold-dim);letter-spacing:.4px}

  .news{position:absolute;left:554px;top:481px;width:210px}
  .news-title{font-size:11.5px;color:var(--gold-dim);letter-spacing:.4px;margin-bottom:6px}
  .news-meta{font-size:9.5px;color:var(--muted);line-height:15.6px}
  .news-body{font-size:9.5px;color:var(--muted-2);line-height:15.6px}
  .news-body a{color:var(--gold-dim)}
  .news-pager{position:absolute;left:553px;top:574px}

  .footer-note{position:absolute;left:553px;top:668px;font-size:9px;color:var(--gold-dim);letter-spacing:.3px}
  .social{position:absolute;top:664px;width:12px;height:12px;background:var(--social)}
</style>
</head>
<body>
  <nav class="main-nav">
    <a class="nav-cell" style="left:552px;top:0;width:114px;background:var(--cell-a)">Apartments</a>
    <a class="nav-cell" style="left:666px;top:0;width:57px;background:var(--cell-b)">Links</a>
    <a class="nav-cell" style="left:723px;top:0;width:114px;background:var(--cell-a)">Reservations</a>
    <a class="nav-cell active" style="left:837px;top:0;width:57px">Home</a>
    <a class="nav-cell" style="left:494px;top:57px;width:58px;background:var(--cell-d)">Rates</a>
    <a class="nav-cell" style="left:552px;top:57px;width:114px;background:var(--cell-c)">Locations</a>
    <a class="nav-cell" style="left:723px;top:57px;width:114px;background:var(--cell-a)">Reviews</a>
  </nav>
  <nav class="sub-nav">
    <a class="nav-sub" style="left:579px">Reviews</a>
    <a class="nav-sub" style="left:660px">Chirpline</a>
    <a class="nav-sub" style="left:752px">Boston</a>
    <a class="nav-sub" style="left:835px">About Us</a>
  </nav>

  <a class="brand" href="#"><span class="brand-mark"></span><span class="brand-name">RIBTEN LOFTS</span></a>

  <div class="slide-photo" role="img" aria-label="Photo of a bright furnished bedroom with warm orange walls"></div>
  <svg class="slide-arrow" style="left:216px" width="22" height="24" viewBox="0 0 22 24"><polyline points="21,1 1,12 21,23" fill="none" stroke="var(--arrow)" stroke-width="1.5"/></svg>
  <svg class="slide-arrow" style="left:963px" width="22" height="24" viewBox="0 0 22 24"><polyline points="1,1 21,12 1,23" fill="none" stroke="var(--arrow)" stroke-width="1.5"/></svg>

  <h1 class="welcome serif">Welcome to Ribten Lofts<br>Furnished Apartments</h1>
  <p class="intro">Ribten Lofts is proud to offer some of the best furnished apartments in Boston. Our locations are in the trendiest area of the city: the South End. In the South End neighborhood, you will find wonderful restaurants, theaters, cafes and artist lofts. Our short term and extended stay apartments are very, very clean.</p>
  <p class="signoff serif">RIBTEN LOFTS TEAM</p>

  <section class="news">
    <h2 class="news-title serif">LATEST NEWS</h2>
    <p class="news-meta">12 Januar 2012 | 25 comments</p>
    <p class="news-body">Strategic Consulting and more<br>Strategic consulting capabilities that reveal and solve operational issues. <a href="#">More...</a></p>
  </section>
  <svg class="news-pager" width="64" height="10" viewBox="0 0 64 10">
    <polyline points="7,1 1,5 7,9" fill="none" stroke="#2c2c2c" stroke-width="1"/>
    <polyline points="57,1 63,5 57,9" fill="none" stroke="#2c2c2c" stroke-width="1"/>
  </svg>

  <footer>
    <p class="footer-note serif">© Ribten Lofts 2010 - All Rights Reserved</p>
    <a class="social" style="left:842px" href="#" aria-label="Social link"></a>
    <a class="social" style="left:861px" href="#" aria-label="Social link"></a>
    <a class="social" style="left:880px" href="#" aria-label="Social link"></a>
  </footer>
</body>
</html>
```